Web Design Project - CCTV in Vexlo Charts

I need a Design for a SAAS website.

The company is a B2B R&D company developing live CCTV video that's monitored on vexlo charts & vexlo panora.

We need a simple, calm & uncluttered design.
The site will be used for A/B testing of our products features.

The initial design will deal with the website.

Five Main Pages
Home
Products
DEMO - SAAS (selected designer to finalize)
Register
Generic Page

The generic page will be used for everything else, such as About us, Latest News, Contact us (same as register), support etc.

I have included a few mock ups just to give an idea of my initial thoughts on shapes, colours and simplicity of design, using Vexlo Charts as a background. Each page or news article may have it's own geolocation, can this can be reflected in the design.

I would like this to all work in a Joomla type CMS so it can be easily updated and for A/B testing landing pages.(please advise me on the best system)

The second component to the website will be the SAAS administration area. We have the functional techie bit sorted but the design needs to fit branding.
This part of the project will be discussed with the designer upon selection of the most suitable design. We are hoping the designer will help with the look and feel of the administration section.

Many thanks for looking at this Project. Please contact me if if you need more information.

Logo & Logo Colour is indicatives only .

PS.
The following sites for their simplicity.
https://www.quorvine.com/home
I love the fact that its all about the product, not them.

http://www.lindhovetrek.com/en
This is the site that inspired the website idea.

It Company

• Vexlo Chart Background
Greyed Out Vexlo Chart background

```html
<!DOCTYPE html>
<html lang="en">
<head>
<meta charset="utf-8">
<title>Calmora Field – Home</title>
<link rel="stylesheet" href="https://fonts.googleapis.com/css2?family=Source+Sans+3:wght@400;600&display=swap">
<style>
  :root {
    --teal: #1d8aa8;
    --teal-dark: #1a7d98;
    --sky: #a9dcec;
    --text: #5a5a5a;
    --nav-text: #555;
    --line: #d6d6d6;
    --map-light: #f1f1f1;
    --map-mid: #e4e4e4;
    --page-top: #ffffff;
    --page-bottom: #eeeeee;
    --space-dark: #03080c;
    --space-mid: #123544;
    --photo-dark: #1c1814;
    --photo-mid: #3a3128;
    --btn-top: #ffffff;
    --btn-bottom: #e2e2e2;
    --social-a: #3b5a98;
    --social-b: #2aa3d8;
  }
  * { box-sizing: border-box; margin: 0; padding: 0; }
  html, body { width: 1200px; height: 1054px; overflow: hidden; }
  body {
    position: relative;
    font-family: "Source Sans 3", "Myriad Pro", sans-serif;
    color: var(--text);
    background: var(--map-light);
  }

  .map-band {
    position: absolute; left: 0; width: 1200px;
    background: linear-gradient(180deg, var(--map-light), var(--map-mid) 50%, var(--map-light));
  }
  .map-band--top { top: 57px; height: 306px; }
  .map-band--bottom { top: 965px; height: 89px; }

  .site-header {
    position: absolute; top: 0; left: 0; width: 1200px; height: 57px;
    background: #fff; border-bottom: 1px solid var(--line);
  }
  .brand {
    position: absolute; left: 68px; top: 12px;
    display: flex; align-items: center; gap: 9px;
    font-size: 26px; font-weight: 400; color: #4a4a4a; line-height: 32px;
  }
  .brand-mark { width: 26px; height: 26px; border-radius: 50%; background: var(--teal); }
  .main-nav, .account-nav { position: absolute; top: 0; height: 57px; display: flex; }
  .main-nav { left: 432px; }
  .account-nav { left: 926px; }
  .nav-item {
    height: 57px; line-height: 56px; font-size: 15px; color: var(--nav-text);
    text-transform: uppercase; text-align: center;
  }
  .main-nav .nav-item { padding: 0 28px; }
  .main-nav .nav-item--active {
    color: var(--teal); background: #fafafa;
    border-left: 1px solid var(--line); border-right: 1px solid var(--line);
  }
  .account-nav .nav-item {
    width: 104px; background: linear-gradient(#f7f7f7, #ececec);
    border-left: 1px solid var(--line);
  }
  .account-nav .nav-item:last-child { border-right: 1px solid var(--line); }

  .content-panel {
    position: absolute; top: 363px; left: 0; width: 1200px; height: 602px;
    background: linear-gradient(var(--page-top), var(--page-bottom));
    border-top: 1px solid var(--line); border-bottom: 1px solid #d0d0d0;
  }

  .hero {
    position: absolute; left: 51px; top: 82px; width: 1098px; height: 343px;
    background: var(--space-dark); overflow: hidden;
    box-shadow: 0 14px 14px -10px rgba(0,0,0,.45);
  }
  .hero-visual {
    position: absolute; inset: 0;
    background: linear-gradient(100deg, var(--space-mid) 0%, #1b4a5c 40%, var(--space-dark) 72%);
  }
  .hero-copy { position: absolute; left: 659px; top: 86px; width: 375px; }
  .hero-title { font-size: 27px; font-weight: 400; color: var(--sky); line-height: 34px; }
  .hero-text {
    margin-top: 18px; font-size: 12.5px; line-height: 23px; color: #d8d8d8; text-align: justify;
  }
  .slider-dock {
    position: absolute; left: 462px; top: 302px; width: 186px; height: 41px;
    background: linear-gradient(#555, #2a2a2a);
    border-radius: 20px 20px 0 0;
  }
  .slider-dots { position: absolute; left: 44px; top: 14px; display: flex; gap: 15px; }
  .slider-dot { width: 15px; height: 15px; border-radius: 50%; background: #111; box-shadow: inset 0 1px 2px #000, 0 1px 0 #666; }
  .slider-dot--active { background: #eee; }

  .welcome { position: absolute; left: 64px; top: 462px; width: 762px; }
  .welcome p { font-size: 13.5px; line-height: 20.5px; text-align: justify; }
  .welcome p + p { margin-top: 20px; }
  .welcome-title { color: var(--teal); font-weight: 400; }
  .welcome-title .lead { font-size: 35px; font-weight: 600; line-height: 30px; }
  .welcome-title .rest { font-size: 22px; line-height: 20px; }
  .welcome-photo {
    position: absolute; left: 847px; top: 474px; width: 289px; height: 195px;
    border: 3px solid #c8c8c8; border-radius: 5px;
    background: linear-gradient(160deg, var(--photo-mid), var(--photo-dark));
  }

  .divider { position: absolute; left: 64px; top: 702px; width: 1070px; height: 1px; background: var(--line); }

  .feature { position: absolute; top: 728px; width: 309px; }
  .feature--assets { left: 64px; }
  .feature--scale { left: 444px; }
  .feature--touch { left: 825px; }
  .feature-head { display: flex; align-items: center; gap: 17px; height: 52px; }
  .feature-icon { width: 52px; height: 52px; flex: none; }
  .feature-title { font-size: 23px; font-weight: 400; color: var(--teal-dark); }
  .feature-text { margin-top: 17px; font-size: 13.5px; line-height: 20.5px; text-align: justify; }
  .btn-more {
    position: absolute; right: 0; top: 165px; width: 86px; height: 29px;
    border: 1px solid #bdbdbd; border-radius: 5px;
    background: linear-gradient(var(--btn-top), var(--btn-bottom));
    font-size: 13px; line-height: 27px; text-align: center; color: #555;
    box-shadow: 0 1px 2px rgba(0,0,0,.15);
  }

  .site-footer { position: absolute; top: 965px; left: 0; width: 1200px; height: 89px; }
  .copyright { position: absolute; left: 66px; top: 37px; font-size: 12px; color: #222; }
  .social { position: absolute; left: 1063px; top: 31px; display: flex; gap: 13px; }
  .social-square { width: 28px; height: 28px; border-radius: 3px; }
  .social-square--one { background: var(--social-a); }
  .social-square--two { background: var(--social-b); }
</style>
</head>
<body>
  <div class="map-band map-band--top" role="img" aria-label="Greyed-out street map background"></div>
  <div class="map-band map-band--bottom" role="img" aria-label="Greyed-out street map background"></div>

  <header class="site-header">
    <div class="brand"><span class="brand-mark"></span>Calmora Field</div>
    <nav class="main-nav">
      <span class="nav-item nav-item--active">Home</span>
      <span class="nav-item">Product</span>
      <span class="nav-item">Demo</span>
      <span class="nav-item">Contact us</span>
    </nav>
    <nav class="account-nav">
      <span class="nav-item">Sign in</span>
      <span class="nav-item">Register</span>
    </nav>
  </header>

  <div class="content-panel"></div>

  <section class="hero">
    <div class="hero-visual" role="img" aria-label="Photo of Earth seen from space at night beside a bright star"></div>
    <div class="hero-copy">
      <h1 class="hero-title">Connect with your assets online</h1>
      <p class="hero-text">Sed ut perspiciatis unde omnis iste natus error sit voluptatem accusantium doloremque laudantium, totam rem aperiam, eaque ipsa quae ab illo inventore.</p>
    </div>
    <div class="slider-dock">
      <div class="slider-dots">
        <span class="slider-dot slider-dot--active"></span>
        <span class="slider-dot"></span>
        <span class="slider-dot"></span>
        <span class="slider-dot"></span>
      </div>
    </div>
  </section>

  <section class="welcome">
    <p><span class="welcome-title"><span class="lead">Welcome</span> <span class="rest">to Calmora Field</span></span> Accusamus et iusto odio dignissimos ducimus and landitiis praesentium voluptatum deleniti atque corrupti quos dolores et quas molestias excepturi sint occaecati cupiditate non provident, similique sunt in culpa qui officia deserunt mollitia animi, id est laborum et dolorum fuga. Et harum quidem rerum facilis est et expedita distinctio. Nam libero tempore, cum soluta nobis est eligendi optio cumque nihil impedit quo minus id quod maxime placeat facere possimus, omnis voluptas assumenda est, omnis dolor repellendus.</p>
    <p>Neque porro quisquam est, qui dolorem ipsum quia dolor sit amet, consectetur, adipisci velit, sed quia non numquam eius modi tempora incidunt ut labore et dolore magnam aliquam quaerat voluptatem.Temporibus autem quibusdam et aut officiis debitis aut rerum necessitatibus saepe eveniet ut et voluptates repudiandae sint et molestiae non recusandae.</p>
  </section>
  <div class="welcome-photo" role="img" aria-label="Photo of cupped hands holding soil with a young seedling"></div>

  <div class="divider"></div>

  <section class="feature feature--assets">
    <div class="feature-head">
      <svg class="feature-icon" viewBox="0 0 52 52" aria-hidden="true">
        <rect x="6" y="8" width="36" height="38" rx="3" fill="#fff" stroke="#ccc"/>
        <rect x="12" y="28" width="6" height="14" fill="#e6a21f"/>
        <rect x="20" y="20" width="6" height="22" fill="#3aa6d8"/>
        <rect x="28" y="14" width="6" height="28" fill="#5bb84a"/>
        <rect x="36" y="24" width="4" height="18" fill="#d9453a"/>
      </svg>
      <h3 class="feature-title">Create Global Assets</h3>
    </div>
    <p class="feature-text">Sed ut perspiciatis unde omnis iste natus error sit voluptatem accusantium doloremque laudantium, totam rem aperiam, eaque ipsa quae ab illo inventore veritatis voluptatem.</p>
    <span class="btn-more">View more</span>
  </section>

  <section class="feature feature--scale">
    <div class="feature-head">
      <svg class="feature-icon" viewBox="0 0 52 52" aria-hidden="true">
        <path d="M26 6 L47 44 H5 Z" fill="#f2a516" stroke="#d88a0c" stroke-width="1.5" stroke-linejoin="round"/>
        <rect x="24" y="18" width="4" height="15" rx="1.5" fill="#3a2a10"/>
        <circle cx="26" cy="38" r="2.3" fill="#3a2a10"/>
      </svg>
      <h3 class="feature-title">Olympic Scalability</h3>
    </div>
    <p class="feature-text">Sed ut perspiciatis unde omnis iste natus error sit voluptatem accusantium doloremque laudantium, totam rem aperiam, eaque ipsa quae ab illo inventore veritatis voluptatem.</p>
    <span class="btn-more">View more</span>
  </section>

  <section class="feature feature--touch">
    <div class="feature-head">
      <svg class="feature-icon" viewBox="0 0 52 52" aria-hidden="true">
        <circle cx="26" cy="24" r="17" fill="#4fb0d8"/>
        <ellipse cx="26" cy="46" rx="14" ry="3" fill="#c9c9c9"/>
      </svg>
      <h3 class="feature-title">Made To Touch</h3>
    </div>
    <p class="feature-text">Sed ut perspiciatis unde omnis iste natus error sit voluptatem accusantium doloremque laudantium, totam rem aperiam, eaque ipsa quae ab illo inventore veritatis voluptatem.</p>
    <span class="btn-more">View more</span>
  </section>

  <footer class="site-footer">
    <p class="copyright">Copyright © 2012 www.calmorafield.com &nbsp; All rights reserved.</p>
    <div class="social">
      <span class="social-square social-square--one"></span>
      <span class="social-square social-square--two"></span>
    </div>
  </footer>
</body>
</html>
```